Newspaper Ad Design Project

Hi there,
Our company Brindle Panels is a manufacturer of kitchen and wardrobe doors. We have 2 markets that we sell to 1. Home owners / renovators who would like to put new doors in their kitchen or built in wardrobes and 2. Kitchen and wardrobe companies who buy their doors from us. I need newspaper ads that will appeal to both these markets. The advertisements are for the Sydney local newspapers.
The successful designer will be asked to create several versions of the design for different sized ads.The first ad will be 9 x 13cm wide.
Most important aspects of the design:
1. Must grab attention. When the page is opened, this ad should be the first thing people notice.
2. Clean, simple design, no clutter.
3. Use company logo and colours
I have attached the logo, our brochure and the old ad for wording reference but we can cut out a lot of the text to keep the ad simple and attention grabbing. I want the new ad to look very different. The most important text for the ad is below.
Headline: Renovating your kitchen?
Subheading: Just replace the doors
sub, sub heading: Saving you thousands of $$$
"Get a quote now at www.brindlepanels-example.com.au"
"DIY measure and install"
8631 2975
Please keep the phone number small and website address bigger so that people go to the website instead of just picking up the phone to ask questions.
Target Market(s)
DIY home renovators and owners and Sydney kitchen and wardrobe companies looking to source doors from us.
Industry/Entity Type
It Company

```html
<!DOCTYPE html>
<html lang="en">
<head>
<meta charset="utf-8">
<title>Brindle Panels – Renovating your kitchen?</title>
<link rel="stylesheet" href="https://fonts.googleapis.com/css2?family=Anton&family=Libre+Baskerville:ital,wght@1,700&family=PT+Sans:wght@700&family=PT+Sans+Narrow:wght@700&display=swap">
<style>
  :root {
    --sun: #fbbb2c;
    --sun-light: #fde38c;
    --red: #e3202a;
    --red-deep: #b3131b;
    --ink: #141414;
    --brown: #3e2114;
    --cream: #fdeeb3;
    --white: #ffffff;
    --seal-blue: #1d4f9c;
    --photo-wall: #c9b49a;
    --photo-floor: #a2532a;
  }
  * { margin: 0; padding: 0; box-sizing: border-box; }
  html, body { width: 1200px; height: 881px; overflow: hidden; background: #ece6dc; }
  .ad {
    position: relative;
    width: 1200px; height: 881px;
    overflow: hidden;
    background: radial-gradient(ellipse at 68% 62%, var(--sun-light) 0%, var(--sun) 62%);
    font-family: "PT Sans", Arial, sans-serif;
    color: var(--ink);
  }
  .headline {
    position: absolute; left: 48px; top: 12px;
    font-family: "Anton", Impact, sans-serif;
    font-size: 104px; line-height: 1.15; font-weight: 400;
    letter-spacing: 0.5px; white-space: nowrap;
  }
  .subheading {
    position: absolute; left: 48px; top: 146px;
    font-family: "Libre Baskerville", Georgia, serif;
    font-style: italic; font-weight: 700;
    font-size: 46px; white-space: nowrap;
  }
  .reasons {
    position: absolute; left: 36px; top: 222px;
    width: 1126px; height: 112px;
    background: linear-gradient(180deg, #f0353d 0%, var(--red) 55%, var(--red-deep) 100%);
    border: 7px solid var(--ink);
    border-radius: 56px;
    padding: 12px 0 0 34px;
    font-family: "PT Sans Narrow", Arial Narrow, sans-serif;
    color: var(--white);
    white-space: nowrap;
  }
  .reasons-title { font-size: 33px; line-height: 1.15; }
  .reasons-title .accent { color: var(--ink); }
  .reasons-list { font-size: 28px; line-height: 1.3; }
  .reasons-list span { margin-right: 10px; }
  .quote-lead {
    position: absolute; left: 42px; top: 363px;
    font-family: "PT Sans Narrow", Arial Narrow, sans-serif;
    font-size: 34px;
  }
  .quote-url {
    position: absolute; left: 42px; top: 404px;
    font-size: 40px; white-space: nowrap;
  }
  .diy {
    position: absolute; left: 42px; top: 478px;
    font-size: 33px;
  }
  .saving-sticker {
    position: absolute; left: 896px; top: 304px;
    width: 288px; height: 288px;
    border-radius: 50%;
    background: radial-gradient(circle at 40% 35%, #ec3a40 0%, var(--red) 55%, var(--red-deep) 100%);
    border: 9px solid var(--cream);
    display: flex; align-items: center; justify-content: center;
    text-align: center;
    font-family: "Anton", Impact, sans-serif;
    font-size: 40px; line-height: 1.02;
    color: var(--white);
    -webkit-text-stroke: 1.5px var(--ink);
    z-index: 2;
  }
  .footer-band {
    position: absolute; left: 0; top: 533px;
    width: 1200px; height: 348px;
    background: var(--brown);
  }
  .kitchen-photo {
    position: absolute; left: 0; top: 533px;
    width: 489px; height: 348px;
    background: linear-gradient(180deg, var(--photo-wall) 0%, #e8e2d8 45%, #f2f0ec 62%, var(--photo-floor) 100%);
  }
  .quality-seal {
    position: absolute; left: 426px; top: 517px;
    width: 164px; height: 164px;
    z-index: 3;
  }
  .brand {
    position: absolute; left: 560px; top: 640px;
    display: flex; align-items: center; gap: 14px;
  }
  .brand-mark { width: 30px; height: 30px; background: var(--cream); }
  .brand-name {
    font-family: "PT Sans", Arial, sans-serif;
    font-weight: 700; font-size: 40px; line-height: 1.05;
    color: var(--cream);
  }
  .contact {
    position: absolute; left: 742px; top: 616px;
    color: var(--white);
    font-size: 24px; line-height: 1.45;
    white-space: nowrap;
  }
  .contact .gap { margin-top: 18px; }
</style>
</head>
<body>
<div class="ad">
  <h1 class="headline">Renovating your kitchen?</h1>
  <p class="subheading">Just Replace the Doors</p>

  <div class="reasons">
    <p class="reasons-title">5 Reasons to <span class="accent">REPLACE</span> Your <span class="accent">KITCHEN DOORS</span> Compared to Full Kitchen Renovation</p>
    <p class="reasons-list"><span>It’s Cheaper,</span><span>It’s Quicker,</span><span>It’s Easier,</span><span>It’s Less Hassle &amp; Mess,</span><span>It’s Less Wastage</span></p>
  </div>

  <p class="quote-lead">Get a quote now at</p>
  <p class="quote-url">www.brindlepanels-example.com.au</p>
  <p class="diy">DIY Measure and Install</p>

  <div class="saving-sticker">Saving<br>You<br>Thousands<br>of<br>$$$</div>

  <div class="footer-band"></div>
  <div class="kitchen-photo" role="img" aria-label="Photo of a bright white kitchen with island bench, stainless steel fridge and timber floor"></div>

  <svg class="quality-seal" viewBox="0 0 164 164" role="img" aria-label="Quality seal">
    <circle cx="82" cy="82" r="78" fill="var(--white)"/>
    <circle cx="82" cy="82" r="70" fill="var(--seal-blue)"/>
    <circle cx="82" cy="82" r="46" fill="var(--white)"/>
  </svg>

  <div class="brand">
    <span class="brand-mark"></span>
    <span class="brand-name">Brindle<br>Panels</span>
  </div>

  <div class="contact">
    <p>14 Callow Street</p>
    <p>KELLERTON NSW 2170</p>
    <p class="gap">P: (02) 8631 2975</p>
    <p>F: (02) 8631 2976</p>
    <p class="gap">E: sales@brindlepanels-example.com.au</p>
  </div>
</div>
</body>
</html>
```